Heal the world with your creativity.

We're looking for advertising materials (social media, email, etc) for a new mental health platform called PIVOT (www.viewpivot.tv). PIVOT’s mission is to empower our members to heal and thrive by making expert advice and real-life experiences accessible to all.

Note

Facebook Cover Images: 820 x 312 pixels
LinkedIn Cover Images: 1128 x 191 pixels
3 x Social Media Post Image Templates: 1080 x 1080 pixles
3 x Enewsletter Header Image Templates: 1080 x 360 pixels
Sales One sheet: US Letter (8.5 x 11 inches)
Overview Powerpoint template: 13.33 x 7.5 inches

Fonts to Use:
Galanogrotesque
Montserrat regular

Target Market(s)

18 - 35 year olds

Industry/Entity Type

Mental Health

Requirements
Must have
• Facebook Cover Images: 820 x 312 pixels
3 x Enewsletter Header Images: 1080 x 360 pixels

Fonts to Use:
Galanogrotesque
Montserrat regular
Nice to have
• Creative copywriting for social media posts

```html
<!DOCTYPE html>
<html lang="en">
<head>
<meta charset="utf-8">
<title>PIVOT – Social Post Template</title>
<link rel="stylesheet" href="https://fonts.googleapis.com/css2?family=Montserrat:wght@200;500;700;800&family=Roboto:wght@400;500;700&display=swap">
<style>
  :root {
    --navy: #0f4b6f;
    --ring: #2a6a91;
    --blue: #2379ab;
    --sky: #3d93c3;
    --mist: #a8cbde;
    --orange: #f47d36;
    --white: #ffffff;
  }
  * { margin: 0; padding: 0; box-sizing: border-box; }
  html, body { width: 1199px; height: 1200px; overflow: hidden; background: var(--navy); }
  .post {
    position: relative;
    width: 1199px;
    height: 1200px;
    background: var(--navy);
    overflow: hidden;
    color: var(--white);
  }
  .decor { position: absolute; inset: 0; }
  .headline {
    position: absolute;
    left: 202px;
    top: 90px;
    font-family: "Montserrat", sans-serif;
    line-height: 1;
  }
  .headline-lead {
    display: block;
    font-weight: 800;
    font-size: 63px;
    letter-spacing: 0.5px;
  }
  .headline-main {
    display: block;
    margin-top: 22px;
    margin-left: -4px;
    font-weight: 200;
    font-size: 146px;
    letter-spacing: 3px;
  }
  .divider {
    position: absolute;
    left: 202px;
    top: 345px;
    width: 612px;
    height: 6px;
    background: var(--blue);
  }
  .intro {
    position: absolute;
    left: 202px;
    top: 376px;
    font-family: "Roboto", sans-serif;
    font-size: 44px;
    font-weight: 400;
  }
  .options {
    position: absolute;
    left: 205px;
    top: 460px;
    list-style: none;
    font-family: "Roboto", sans-serif;
    font-weight: 500;
    font-size: 38px;
    color: var(--orange);
  }
  .options li {
    display: flex;
    align-items: center;
    height: 64.5px;
  }
  .options li::before {
    content: "";
    width: 22px;
    height: 22px;
    border-radius: 50%;
    background: var(--orange);
    margin-right: 25px;
  }
  .cta {
    position: absolute;
    left: 884px;
    top: 686px;
    width: 343px;
    text-align: center;
    font-family: "Roboto", sans-serif;
    font-weight: 700;
    font-size: 38px;
    line-height: 49px;
    color: var(--navy);
  }
  .brand-badge {
    position: absolute;
    left: 50px;
    top: 724px;
    width: 228px;
    height: 228px;
    border-radius: 50%;
    background: var(--white);
    box-shadow: 0 4px 14px rgba(0, 0, 0, 0.25);
    display: flex;
    align-items: center;
    justify-content: center;
    font-family: "Montserrat", sans-serif;
    font-weight: 800;
    font-size: 48px;
    color: var(--orange);
  }
  .tagline {
    position: absolute;
    left: 765px;
    top: 1018px;
    font-family: "Montserrat", sans-serif;
  }
  .tagline-small {
    display: block;
    font-weight: 500;
    font-size: 19px;
    letter-spacing: 0.6px;
  }
  .tagline-big {
    display: block;
    margin-top: 4px;
    font-weight: 800;
    font-size: 42px;
    line-height: 1.1;
  }
  .website {
    display: block;
    margin-top: 6px;
    font-weight: 500;
    font-size: 25px;
    color: var(--orange);
  }
  .social {
    position: absolute;
    left: 765px;
    top: 1142px;
    display: flex;
    gap: 21px;
  }
  .social span {
    width: 38px;
    height: 38px;
    border-radius: 50%;
    background: var(--blue);
  }
</style>
</head>
<body>
<main class="post">
  <svg class="decor" width="1199" height="1200" viewBox="0 0 1199 1200" aria-hidden="false">
    <defs>
      <clipPath id="sun-clip"><circle cx="1043" cy="28" r="111"/></clipPath>
      <radialGradient id="portrait-tone" cx="45%" cy="40%" r="70%">
        <stop offset="0" stop-color="#e0a873"/>
        <stop offset="0.5" stop-color="#b7844f"/>
        <stop offset="1" stop-color="#6d5a3a"/>
      </radialGradient>
    </defs>

    <!-- top corner accents -->
    <circle cx="1124" cy="111" r="42" fill="var(--blue)"/>
    <circle cx="1043" cy="28" r="111" fill="var(--orange)"/>
    <circle cx="1124" cy="111" r="42" fill="#ffffff" opacity="0.35" clip-path="url(#sun-clip)"/>

    <!-- call to action disc -->
    <circle cx="1055" cy="738" r="172" fill="var(--mist)"/>

    <!-- portrait frame -->
    <circle cx="383" cy="1011" r="290" fill="var(--ring)"/>
    <circle cx="383" cy="1010" r="235" fill="url(#portrait-tone)" role="img" aria-label="Photo of a young woman in a warm jacket outdoors in autumn sunlight"/>
    <circle cx="566" cy="1199" r="128" fill="var(--sky)" opacity="0.85"/>
    <circle cx="611" cy="953" r="26" fill="var(--orange)"/>
    <circle cx="699" cy="1142" r="11" fill="var(--white)"/>
  </svg>

  <h1 class="headline">
    <span class="headline-lead">TITLE WILL</span>
    <span class="headline-main">BE HERE</span>
  </h1>
  <div class="divider"></div>
  <p class="intro">More information will be here.</p>
  <ul class="options">
    <li>Option 1</li>
    <li>Option 2</li>
    <li>Option 3</li>
  </ul>

  <p class="cta">Call of Action<br>Will be Here</p>

  <div class="brand-badge">PIVOT</div>

  <div class="tagline">
    <span class="tagline-small">YOUR MENTAL HEALTH</span>
    <span class="tagline-big">MADE SIMPLE.</span>
    <span class="website">www.viewpivot.tv</span>
  </div>
  <div class="social" aria-label="Social channels">
    <span></span><span></span><span></span>
  </div>
</main>
</body>
</html>
```